Graphic Design/Logo Needed for Ear Drops Bottle

We have an Ear Drop Medication that we need to create a new label for. We will use a retro picture of a Doctor (Dr. Blenham) and the name of the product is Tidy Lobe. There is no official logo, so we will want to create a retro, basic logo for Tidy Lobe and use the retro picture. Front portion of the label is Size is 1.5" in height, and about 1.375" Width. this is a small tube similar in size to eye drops. We will be looking for just the logo portion and what you will see on the front of the bottle.

Target Market(s)

Medical Container

Industry/Entity Type

Medical

Font styles to use
Serif
Sans Serif

Colors
0054AA
0677BA
7BADD7
CADEEF
E8F1F8
FFF300
FFF600
FEFA6F
FFFEC7
FFFEE8

Requirements
Must have
• Picture of Dr. Blenham, "Tidy Lobe", Dr. Blenham's Ear Solution
Nice to have
• Retro Style or Modern with Retro Feel, Clean and engaging

```html
<!DOCTYPE html>
<html lang="en">
<head>
<meta charset="UTF-8">
<title>Tidy Lobe – Dr. Blenham's Ear Solution</title>
<link href="https://fonts.googleapis.com/css2?family=Shrikhand&family=Alfa+Slab+One&display=swap" rel="stylesheet">
<style>
  :root {
    --navy: #2d2e4f;
    --cream: #fdf7ea;
    --teal: #67a6b5;
    --teal-light: #86bac6;
    --pink: #e595a0;
    --red: #ea5644;
    --orange: #ef8a24;
    --yellow: #ecce4c;
    --sky-edge: #7fb3c1;
    --sky-center: #eef0e4;
    --sepia-light: #bdb2a0;
    --sepia-dark: #6e665a;
  }
  html, body {
    margin: 0;
    padding: 0;
    overflow: hidden;
    background: var(--sky-edge);
  }
  .label {
    width: 1100px;
    height: 1200px;
    position: relative;
    overflow: hidden;
  }
  .label svg { display: block; }
  .title-text {
    font-family: "Shrikhand", cursive;
    font-size: 178px;
    text-anchor: middle;
    stroke-linejoin: round;
    paint-order: stroke fill;
  }
  .bubble-text {
    font-family: "Alfa Slab One", serif;
    fill: var(--navy);
    text-anchor: middle;
  }
</style>
</head>
<body>
<div class="label">
  <svg width="1100" height="1200" viewBox="0 0 1100 1200" xmlns="http://www.w3.org/2000/svg">
    <defs>
      <radialGradient id="sky" cx="0.5" cy="0.55" r="0.75">
        <stop offset="0" stop-color="var(--sky-center)"/>
        <stop offset="0.55" stop-color="#cfe0dc"/>
        <stop offset="1" stop-color="var(--sky-edge)"/>
      </radialGradient>
      <linearGradient id="screen" x1="0" y1="0" x2="1" y2="1">
        <stop offset="0" stop-color="var(--teal-light)"/>
        <stop offset="1" stop-color="var(--teal)"/>
      </linearGradient>
      <linearGradient id="portrait" x1="0" y1="0" x2="0" y2="1">
        <stop offset="0" stop-color="var(--sepia-dark)"/>
        <stop offset="0.4" stop-color="var(--sepia-light)"/>
        <stop offset="1" stop-color="#d8d0c0"/>
      </linearGradient>
    </defs>

    <!-- sky -->
    <rect class="sky" width="1100" height="1200" fill="url(#sky)"/>

    <!-- rainbow stripes -->
    <g class="stripes" stroke="#dfe8e2" stroke-width="3">
      <polygon fill="var(--teal)"   points="300,0 400,0 400,773 250,1200 60,1200 300,773"/>
      <polygon fill="var(--pink)"   points="400,0 502,0 502,773 458,1200 250,1200 400,773"/>
      <polygon fill="var(--red)"    points="502,0 603,0 603,773 643,1200 458,1200 502,773"/>
      <polygon fill="var(--orange)" points="603,0 704,0 704,773 845,1200 643,1200 603,773"/>
      <polygon fill="var(--yellow)" points="704,0 800,0 800,773 1041,1200 845,1200 704,773"/>
    </g>

    <!-- screen frame -->
    <g class="screen-frame" transform="rotate(-3 580 490)">
      <rect x="210" y="234" width="771" height="533" rx="62" fill="var(--teal)"/>
      <rect x="206" y="230" width="771" height="533" rx="62" fill="var(--yellow)"/>
      <rect x="201" y="225" width="771" height="533" rx="62" fill="var(--orange)"/>
      <rect x="196" y="220" width="771" height="533" rx="62" fill="var(--navy)"/>
      <rect x="207" y="231" width="749" height="511" rx="52" fill="var(--cream)"/>
      <rect x="222" y="246" width="719" height="481" rx="40" fill="var(--teal)"/>
      <rect x="230" y="252" width="707" height="467" rx="36" fill="url(#screen)"/>
    </g>

    <!-- portrait area -->
    <path class="portrait" role="img" aria-label="Retro sepia photograph of Dr. Blenham wearing a head mirror and white coat"
      d="M234,706 L234,652 L330,618 L440,580 L478,545 L452,470 L420,360 L430,250 L470,160 L560,122 L640,138 L702,198 L722,318 L704,420 L690,500 L720,558 L820,600 L932,640 L932,700 Z"
      fill="url(#portrait)" stroke="var(--cream)" stroke-width="6" stroke-linejoin="round"/>

    <!-- speech bubble -->
    <g class="speech-bubble">
      <path transform="translate(0 10)" d="M120,296 Q86,300 90,340 L104,462 Q108,500 146,496 L292,482 L450,562 L392,466 L420,462 Q450,458 446,420 L432,292 Q428,254 390,258 Z"
        fill="var(--navy)" stroke="var(--navy)" stroke-width="14" stroke-linejoin="round"/>
      <path d="M120,296 Q86,300 90,340 L104,462 Q108,500 146,496 L292,482 L450,562 L392,466 L420,462 Q450,458 446,420 L432,292 Q428,254 390,258 Z"
        fill="var(--cream)" stroke="var(--navy)" stroke-width="13" stroke-linejoin="round"/>
      <g transform="rotate(-6 268 380)">
        <text class="bubble-text" x="268" y="338" font-size="31">Dr. Blenham's</text>
        <text class="bubble-text" x="268" y="413" font-size="82">EAR</text>
        <text class="bubble-text" x="268" y="450" font-size="34" letter-spacing="1">SOLUTION</text>
      </g>
    </g>

    <!-- sparkles -->
    <g class="sparkles" fill="var(--navy)">
      <path d="M265,975 Q270,1013 308,1018 Q270,1023 265,1061 Q260,1023 222,1018 Q260,1013 265,975 Z"/>
      <path d="M836,934 Q841,971 879,976 Q841,981 836,1018 Q831,981 793,976 Q831,971 836,934 Z"/>
    </g>

    <!-- product name -->
    <g class="product-name">
      <g aria-hidden="true">
        <text class="title-text" x="572" y="946" fill="var(--teal)" stroke="var(--teal)" stroke-width="30">Tidy</text>
        <text class="title-text" x="572" y="1086" fill="var(--teal)" stroke="var(--teal)" stroke-width="30">Lobe</text>
        <text class="title-text" x="567" y="941" fill="var(--yellow)" stroke="var(--yellow)" stroke-width="30">Tidy</text>
        <text class="title-text" x="567" y="1081" fill="var(--yellow)" stroke="var(--yellow)" stroke-width="30">Lobe</text>
        <text class="title-text" x="563" y="937" fill="var(--orange)" stroke="var(--orange)" stroke-width="30">Tidy</text>
        <text class="title-text" x="563" y="1077" fill="var(--orange)" stroke="var(--orange)" stroke-width="30">Lobe</text>
      </g>
      <text class="title-text" x="558" y="932" fill="var(--cream)" stroke="var(--navy)" stroke-width="28">Tidy</text>
      <text class="title-text" x="558" y="1072" fill="var(--cream)" stroke="var(--navy)" stroke-width="28">Lobe</text>
    </g>
  </svg>
</div>
</body>
</html>
```